Looking for a professional, clean and crisp business card

I am in the underground utilities industry and am just looking for a really impressive business card. I would like our card to be white with our symbol crisp and clear with it protruding. I also have a business partner that will require his name and info on the card once the design is set. I would like to have our website info on the card which is;
http://granitetrenchco.example/

Contact Information for Business Card

Website, contact name, number and email

```html
<!DOCTYPE html>
<html lang="en">
<head>
<meta charset="utf-8">
<title>Granite Trench Co — Business Card</title>
<link rel="stylesheet" href="https://fonts.googleapis.com/css2?family=Barlow+Condensed:wght@500;600;700&display=swap">
<style>
  :root {
    --backdrop: #bdbebf;
    --brand-blue: #3b5ea6;
    --photo-blue-top: #6479b4;
    --photo-blue-bottom: #4a63a6;
    --ink: #1f1f21;
    --paper: #ffffff;
    --rule: #9a9a9a;
  }
  * { box-sizing: border-box; margin: 0; padding: 0; }
  html, body {
    width: 1026px;
    height: 1200px;
    overflow: hidden;
    background: var(--backdrop);
    font-family: "Barlow Condensed", "Arial Narrow", sans-serif;
  }
  .sheet { position: relative; width: 1026px; height: 1200px; }

  /* Front card */
  .card-front {
    position: absolute;
    left: 29px; top: 39px;
    width: 969px; height: 554px;
    overflow: hidden;
    border-top: 2px solid var(--brand-blue);
  }
  .card-front__photo {
    position: absolute; inset: 0;
    background: linear-gradient(180deg, var(--photo-blue-top) 0%, var(--photo-blue-bottom) 100%);
  }
  .card-front__brand {
    position: absolute;
    left: 0; right: 0; top: 248px;
    display: flex; align-items: center; justify-content: center; gap: 16px;
  }
  .brand-dot {
    width: 34px; height: 34px; border-radius: 50%;
  }
  .card-front .brand-dot { background: var(--paper); }
  .brand-name {
    font-weight: 700;
    font-size: 52px;
    letter-spacing: 2px;
    text-transform: uppercase;
    line-height: 1;
  }
  .card-front .brand-name { color: var(--paper); }
  .card-front__website {
    position: absolute;
    left: 0; right: 0; top: 514px;
    text-align: center;
    color: var(--paper);
    font-weight: 600;
    font-size: 23px;
    letter-spacing: 0.5px;
    text-transform: uppercase;
  }

  /* Back card */
  .card-back {
    position: absolute;
    left: 29px; top: 610px;
    width: 969px; height: 560px;
    background: var(--paper);
    overflow: hidden;
  }
  .card-back__brand {
    position: absolute;
    left: 0; right: 0; top: 146px;
    display: flex; align-items: center; justify-content: center; gap: 14px;
  }
  .card-back .brand-dot { background: var(--brand-blue); width: 28px; height: 28px; }
  .card-back .brand-name { color: var(--ink); font-size: 44px; }

  .person {
    position: absolute;
    left: 260px; top: 355px;
  }
  .person__name {
    color: var(--ink);
    font-weight: 700;
    font-size: 23px;
    letter-spacing: 0.5px;
    text-transform: uppercase;
    line-height: 1.1;
  }
  .person__role {
    color: var(--brand-blue);
    font-weight: 600;
    font-size: 17px;
    letter-spacing: 0.5px;
    text-transform: uppercase;
    margin-top: 4px;
  }
  .divider {
    position: absolute;
    left: 484px; top: 322px;
    width: 1px; height: 117px;
    background: var(--rule);
  }
  .contact-list {
    position: absolute;
    left: 522px; top: 337px;
    list-style: none;
  }
  .contact-list__item {
    display: flex; align-items: center; gap: 14px;
    height: 26px;
    margin-bottom: 15px;
    color: var(--ink);
    font-weight: 600;
    font-size: 18px;
    letter-spacing: 0.4px;
    text-transform: uppercase;
  }
  .contact-icon {
    width: 25px; height: 25px;
    background: var(--brand-blue);
    display: flex; align-items: center; justify-content: center;
    flex: none;
  }
  .contact-icon svg { width: 15px; height: 15px; }

  .footer-band {
    position: absolute;
    left: 0; right: 0; bottom: 0;
    height: 29px;
    display: flex;
  }
  .footer-band__blue { width: 484px; background: var(--brand-blue); }
  .footer-band__dark { flex: 1; background: var(--ink); }
</style>
</head>
<body>
<main class="sheet">

  <section class="card-front">
    <div class="card-front__photo" role="img" aria-label="Blue-toned photo of an underground utilities crew working on a road trench beside apartment buildings and a drilling rig"></div>
    <div class="card-front__brand">
      <span class="brand-dot"></span>
      <span class="brand-name">Granite Trench Co</span>
    </div>
    <p class="card-front__website">www.granitetrenchco.example</p>
  </section>

  <section class="card-back">
    <div class="card-back__brand">
      <span class="brand-dot"></span>
      <span class="brand-name">Granite Trench Co</span>
    </div>

    <div class="person">
      <p class="person__name">Dale Merriott</p>
      <p class="person__role">Owner</p>
    </div>

    <div class="divider"></div>

    <ul class="contact-list">
      <li class="contact-list__item">
        <span class="contact-icon">
          <svg viewBox="0 0 24 24" fill="#fff" aria-hidden="true"><path d="M6.6 10.8a15.1 15.1 0 0 0 6.6 6.6l2.2-2.2a1 1 0 0 1 1-.25 11.4 11.4 0 0 0 3.6.57 1 1 0 0 1 1 1V20a1 1 0 0 1-1 1A17 17 0 0 1 3 4a1 1 0 0 1 1-1h3.5a1 1 0 0 1 1 1c0 1.25.2 2.45.57 3.57a1 1 0 0 1-.25 1z"/></svg>
        </span>
        555-014-2290
      </li>
      <li class="contact-list__item">
        <span class="contact-icon">
          <svg viewBox="0 0 24 24" fill="#fff" aria-hidden="true"><path d="M3 5h18v14H3z M4.5 6.5 12 12l7.5-5.5" stroke="#3b5ea6" stroke-width="1.6" stroke-linejoin="round"/></svg>
        </span>
        dale@granitetrenchco.example
      </li>
      <li class="contact-list__item">
        <span class="contact-icon">
          <svg viewBox="0 0 24 24" fill="none" stroke="#fff" stroke-width="2" aria-hidden="true"><circle cx="12" cy="12" r="9"/><path d="M3 12h18M12 3c3 3.2 3 14.8 0 18M12 3c-3 3.2-3 14.8 0 18"/></svg>
        </span>
        www.granitetrenchco.example
      </li>
    </ul>

    <div class="footer-band">
      <span class="footer-band__blue"></span>
      <span class="footer-band__dark"></span>
    </div>
  </section>

</main>
</body>
</html>
```